Golden Years Wellness Roadmap: This is my second book. The first was Eldercare Compass

I need a book cover design for: GOLDEN YEARS WELLNESS ROADMAP: A NO-EXPENSE METHOD FOR FINISHING YOUR LATER-LIFE MOSAIC WITH POOLED KVB CARE SCHEMES by Derek Holloway Neil Osgrove & Martin Quarles. This book is designed for business owners, CEO's, CFO's and Human Resources. The cover needs to be professional and focused on business. The purpose of this book is to educate business owners and their management about a zero cost retiree health plan. This is a first of it's kind solution that every business needs to learn about.

Target Market(s)

Business owners, CEO's, CFO's and Human Resources

Requirements
Nice to have
• I want the design to be clean and professional since it is focused on business executives

```html
<!DOCTYPE html>
<html lang="en">
<head>
<meta charset="utf-8">
<title>Golden Years Wellness Roadmap — Book Cover</title>
<link href="https://fonts.googleapis.com/css2?family=Montserrat:wght@800;900&family=Barlow+Condensed:wght@300;400;500;600&display=swap" rel="stylesheet">
<style>
  :root {
    --page: #ffffff;
    --paper: #eef0f3;
    --paper-light: #f8f9fb;
    --navy: #0c2d5e;
    --bright-blue: #1474c0;
    --ink-blue: #1f4f86;
    --rule: #1b2838;
    --band-top: #13608f;
    --band-bottom: #0b5586;
    --white: #ffffff;
  }
  html, body {
    margin: 0;
    padding: 0;
    width: 1200px;
    height: 1200px;
    overflow: hidden;
    background: var(--page);
  }
  .canvas {
    position: relative;
    width: 1200px;
    height: 1200px;
    background: var(--page);
  }
  .book-cover {
    position: absolute;
    left: 221px;
    top: 32px;
    width: 758px;
    height: 1136px;
    overflow: hidden;
    background: radial-gradient(ellipse at 55% 45%, var(--paper-light) 0%, var(--paper) 75%, #e4e8ed 100%);
  }
  .grid-backdrop {
    position: absolute;
    inset: 0;
    background: radial-gradient(ellipse at 50% 40%, rgba(255,255,255,0.7) 0%, rgba(220,226,234,0.35) 100%);
  }
  .puzzle-art {
    position: absolute;
    left: 186px;
    top: 121px;
    width: 382px;
    height: 335px;
    border: 1.5px solid #5a6470;
    box-sizing: border-box;
    background: linear-gradient(135deg, #f7f8fa 0%, #e9ecf0 55%, #dde2e8 100%);
    box-shadow: 0 6px 18px rgba(60,70,90,0.18);
  }
  .puzzle-piece-accent {
    position: absolute;
    left: 154px;
    top: 102px;
    width: 143px;
    height: 139px;
    background: linear-gradient(160deg, #1f64b4 0%, #0f4f9a 100%);
    border-radius: 4px;
  }
  .title {
    margin: 0;
    font-family: 'Montserrat', sans-serif;
    font-weight: 900;
    line-height: 1;
  }
  .title-line {
    position: absolute;
    left: 0;
    width: 100%;
    text-align: center;
    white-space: nowrap;
    color: var(--navy);
    letter-spacing: -1px;
  }
  .title-line--one { top: 516px; font-size: 70px; }
  .title-line--two { top: 601px; font-size: 90px; }
  .title-line--accent {
    top: 683px;
    font-size: 104px;
    color: var(--bright-blue);
    letter-spacing: -2px;
  }
  .title-rule {
    position: absolute;
    left: 66px;
    width: 626px;
    top: 812px;
    height: 1.5px;
    background: var(--rule);
  }
  .subtitle {
    position: absolute;
    left: 0;
    width: 100%;
    top: 838px;
    margin: 0;
    text-align: center;
    font-family: 'Barlow Condensed', sans-serif;
    font-weight: 300;
    font-size: 28px;
    line-height: 34px;
    color: var(--ink-blue);
  }
  .subtitle strong {
    font-weight: 600;
    color: var(--navy);
  }
  .subtitle-rule {
    position: absolute;
    left: 134px;
    width: 517px;
    top: 943px;
    height: 1px;
    background: var(--ink-blue);
  }
  .audience {
    position: absolute;
    left: 0;
    width: 100%;
    top: 958px;
    margin: 0;
    text-align: center;
    font-family: 'Barlow Condensed', sans-serif;
    font-weight: 400;
    font-size: 21px;
    color: var(--navy);
  }
  .band-rule {
    position: absolute;
    left: 0;
    width: 100%;
    top: 1018px;
    height: 1px;
    background: #4c5966;
  }
  .author-band {
    position: absolute;
    left: 0;
    width: 100%;
    top: 1026px;
    height: 101px;
    background: linear-gradient(180deg, var(--band-top) 0%, var(--band-bottom) 100%);
    display: flex;
    align-items: center;
    justify-content: center;
  }
  .authors {
    margin: 0;
    font-family: 'Barlow Condensed', sans-serif;
    font-weight: 600;
    font-size: 35px;
    letter-spacing: 0.3px;
    color: var(--white);
    white-space: nowrap;
  }
  .authors .divider {
    margin: 0 7px;
  }
</style>
</head>
<body>
<div class="canvas">
  <section class="book-cover">
    <div class="grid-backdrop" role="img" aria-label="Faint architectural blueprint line drawing covering the background"></div>

    <div class="puzzle-art" role="img" aria-label="White jigsaw puzzle square with one blue piece being placed into the last gap">
      <div class="puzzle-piece-accent"></div>
    </div>

    <h1 class="title">
      <span class="title-line title-line--one">GOLDEN YEARS</span>
      <span class="title-line title-line--two">WELLNESS</span>
      <span class="title-line title-line--accent">ROADMAP</span>
    </h1>

    <div class="title-rule"></div>

    <p class="subtitle">A <strong>No-Expense</strong> Method for Finishing Your Later-Life<br>Mosaic with Pooled KVB Care Schemes</p>

    <div class="subtitle-rule"></div>

    <p class="audience">The Essential Guide for Business Owners, CEO's, CFO's &amp; HR Professionals</p>

    <div class="band-rule"></div>

    <div class="author-band">
      <p class="authors">DEREK HOLLOWAY<span class="divider">·</span>NEIL OSGROVE<span class="divider">·</span>MARTIN QUARLES</p>
    </div>
  </section>
</div>
</body>
</html>
```